Terra Swift Business Card Design

We need to improve the design of our current business card. We are a erosion control, hydro seeding company that serves many markets. We are attaching the current business card and our logo as reference. You may also visit our site at www.terraswiftllc.example to reference.

```html
<!DOCTYPE html>
<html lang="en">
<head>
<meta charset="utf-8">
<title>Terra Swift Business Card</title>
<link rel="stylesheet" href="https://fonts.googleapis.com/css2?family=Open+Sans:wght@400;600;700;800&display=swap">
<style>
  :root {
    --stage: #222222;
    --paper: #ffffff;
    --forest: #3f6e5e;
    --leaf: #1fa36a;
    --leaf-deep: #17925c;
    --leaf-light: #2bb074;
    --ink: #1c1c1c;
    --white: #ffffff;
  }
  * { box-sizing: border-box; margin: 0; padding: 0; }
  html, body {
    width: 1200px; height: 780px; overflow: hidden;
    background: var(--stage);
    font-family: "Open Sans", Arial, sans-serif;
  }
  .sheet {
    width: 1200px; height: 780px;
    display: flex; align-items: center; justify-content: center; gap: 40px;
  }
  .card {
    position: relative; width: 540px; height: 309px; overflow: hidden;
    border-radius: 3px;
    box-shadow: 0 12px 30px rgba(0,0,0,.5);
  }

  /* Front */
  .card-front { background: var(--paper); }
  .front-wave { position: absolute; inset: 0; }
  .brand-name {
    position: absolute; left: 34px; top: 52px;
    display: flex; align-items: center; gap: 10px;
    font-size: 30px; font-weight: 800; color: var(--forest); letter-spacing: -0.5px;
  }
  .brand-dot { width: 16px; height: 16px; border-radius: 50%; background: var(--leaf); }
  .address {
    position: absolute; left: 22px; bottom: 22px;
    font-size: 12px; color: var(--white); letter-spacing: .2px;
  }
  .divider {
    position: absolute; left: 268px; top: 70px; width: 1px; height: 120px; background: var(--leaf);
  }
  .details { position: absolute; left: 290px; top: 40px; }
  .person-name { font-size: 27px; font-weight: 700; line-height: 1.05; color: var(--forest); letter-spacing: .5px; }
  .person-name .surname { color: var(--leaf); }
  .person-title { font-size: 13px; color: var(--ink); margin-top: 3px; }
  .office { margin-top: 6px; font-size: 12.5px; font-weight: 600; color: var(--leaf); line-height: 1.3; }
  .contacts { list-style: none; margin-top: 10px; }
  .contacts li {
    display: flex; align-items: center; gap: 7px;
    font-size: 12.5px; color: var(--ink); line-height: 1.55;
  }
  .contacts .tag { color: var(--leaf); }
  .contacts svg { width: 11px; height: 11px; flex: none; }

  /* Back */
  .card-back { color: var(--white); }
  .back-field {
    position: absolute; inset: 0;
    background: radial-gradient(ellipse at 50% 40%, var(--leaf-light), var(--leaf-deep));
  }
  .back-brand {
    position: absolute; left: 0; right: 0; top: 52px;
    display: flex; justify-content: center; align-items: center; gap: 12px;
    font-size: 44px; font-weight: 800; color: var(--forest); letter-spacing: -1px;
  }
  .back-brand .brand-dot { width: 22px; height: 22px; background: var(--forest); }
  .offer { position: absolute; left: 0; right: 0; top: 140px; display: flex; justify-content: center; }
  .offer-col { width: 170px; }
  .offer-col h3 { font-size: 12.5px; font-weight: 700; margin-bottom: 3px; }
  .offer-col ul { list-style: none; }
  .offer-col li { font-size: 11.5px; line-height: 1.45; display: flex; align-items: center; gap: 6px; }
  .offer-col li::before { content: ""; width: 6px; height: 6px; border-radius: 50%; background: var(--white); flex: none; }
  .offer-services { text-align: right; padding-right: 16px; }
  .offer-services li { justify-content: flex-end; flex-direction: row-reverse; }
  .offer-markets { padding-left: 16px; }
  .offer-rule { width: 1px; background: rgba(255,255,255,.6); }
</style>
</head>
<body>
<main class="sheet">

  <section class="card card-front" aria-label="Business card front">
    <svg class="front-wave" viewBox="0 0 540 309" preserveAspectRatio="none" aria-hidden="true">
      <path d="M0,112 C110,100 175,160 225,225 C265,278 330,309 420,309 L0,309 Z" fill="var(--forest)"/>
      <path d="M0,104 C118,92 186,150 236,218 C276,272 340,300 430,303 C345,294 288,266 246,212 C196,146 128,94 0,104 Z" fill="var(--leaf)"/>
    </svg>
    <div class="brand-name"><span>Terra Swift</span><span class="brand-dot"></span></div>
    <p class="address">72 Briarwood Lane, Oak Hollow, NC 28000</p>
    <div class="divider"></div>
    <div class="details">
      <h1 class="person-name">DALE <span class="surname">WHITMORE</span></h1>
      <p class="person-title">Chief Operating Officer</p>
      <p class="office">CORPORATE HEADQUARTERS<br>Terra Swift LLC</p>
      <ul class="contacts">
        <li><svg viewBox="0 0 12 12"><rect x="3" y="1" width="6" height="10" rx="1" fill="none" stroke="var(--forest)" stroke-width="1.2"/></svg>555-210-0143 <span class="tag">(Cell)</span></li>
        <li><svg viewBox="0 0 12 12"><path d="M3,1 L5,3.5 L4,5 C5,7 5.5,7.5 7,8 L8.5,7 L11,9 L9.5,11 C5,10.5 1.5,7 1,2.5 Z" fill="var(--forest)"/></svg>555-210-0187 <span class="tag">(Office)</span></li>
        <li><svg viewBox="0 0 12 12"><circle cx="6" cy="6" r="5" fill="none" stroke="var(--leaf)" stroke-width="1.2"/><path d="M1,6 H11 M6,1 C3,4 3,8 6,11 C9,8 9,4 6,1" fill="none" stroke="var(--leaf)" stroke-width="1"/></svg>www.terraswiftllc.example</li>
        <li><svg viewBox="0 0 12 12"><rect x="1" y="2.5" width="10" height="7" fill="none" stroke="var(--forest)" stroke-width="1.2"/><path d="M1,2.5 L6,6.5 L11,2.5" fill="none" stroke="var(--forest)" stroke-width="1.2"/></svg>dale@terraswiftllc.example</li>
      </ul>
    </div>
  </section>

  <section class="card card-back" aria-label="Business card back">
    <div class="back-field" role="img" aria-label="Green background with a repeating leaf pattern"></div>
    <div class="back-brand"><span>Terra Swift</span><span class="brand-dot"></span></div>
    <div class="offer">
      <div class="offer-col offer-services">
        <h3>Services</h3>
        <ul>
          <li>Erosion Control</li>
          <li>Seeding &amp; Mulching</li>
          <li>Hydroseeding</li>
          <li>Compost Blankets</li>
          <li>Site Prep</li>
          <li>Restoration</li>
        </ul>
      </div>
      <div class="offer-rule"></div>
      <div class="offer-col offer-markets">
        <h3>Markets</h3>
        <ul>
          <li>Solar &amp; Wind</li>
          <li>Oil &amp; Gas</li>
          <li>Brenwick</li>
          <li>Power Plants</li>
          <li>Private Development</li>
          <li>Mine Sites</li>
        </ul>
      </div>
    </div>
  </section>

</main>
</body>
</html>
```